Tri Fold - Restaurant Brochure & pdf multipage

Develop a product guide specific to "restaurant owners" for our company's restaurant insurance services. It will need to be eye-catching, personal, unique, and industry-specific. Several Insurance flyers from our companies are attached for review. We are happy to provide guidance along the way. Our website is www.kovalenbrokerage.example. Please grab logos etc. from there. We can provide other files and more detailed copy.

Target Market(s)

Restaurant owners and CFO's

Industry/Entity Type

Insurance Broker

Font styles to use
Other font styles liked:
• match website fonts

Requirements
Must have
• WE WILL PROVIDE DETAILED CONTENT! AT THIS TIME WE ARE LOOKING FOR THE BASIC DESIGN AND LAYOUT.

EYE-CATCHING MODERN DESIGN WITH IMAGES AND BRANDED FEEL. must be print-ready and set up as a PDF to email.

brief description of our agency and its personal boutique feel specializing in the restaurant market. Also, offer a full-service solution to no only manage their business but personal risks too.

Coverages that need to be listed with a brief description: (See attached Flyers)
General Liability
FF&E (Furniture, Fixtures, and Equipment), Property
Workers Compensation
Umbrella
Liquor Liability
Auto
Cyber
Bonds
EPLI

Carrier List:
The Wexmoor
Bastion
Ferrow Common
Wayfarers
Plains Motor
Quorra
DELVA
Holloway
CountyFirst
KTO
And many more
Nice to have
• carrier logos if room.
Should not have
• TO BE DETERMINED.

```html
<!DOCTYPE html>
<html lang="en">
<head>
<meta charset="utf-8">
<title>Kovalen Brokerage – Independent Risk Advisors</title>
<link href="https://fonts.googleapis.com/css2?family=EB+Garamond:wght@400;500;600;700&display=swap" rel="stylesheet">
<style>
  :root {
    --page-bg: #e6e1d9;
    --red: #cf2e2b;
    --red-deep: #b92623;
    --charcoal: #3a3a3c;
    --white: #ffffff;
    --ink: #2a2a2a;
    --paper-shade: #ececec;
    --serif: "EB Garamond", Georgia, serif;
  }
  * { box-sizing: border-box; margin: 0; padding: 0; }
  html, body { width: 1059px; height: 1200px; overflow: hidden; }
  body { background: var(--page-bg); font-family: var(--serif); }

  .flyer {
    position: absolute; left: 100px; top: 0;
    width: 859px; height: 1200px; overflow: hidden;
    background: linear-gradient(90deg, var(--white) 55%, var(--paper-shade) 100%);
  }
  .flyer svg.backdrop { position: absolute; inset: 0; }

  .headline {
    position: absolute; right: 47px; top: 40px; text-align: right;
    color: var(--white); font-weight: 600; font-size: 63px; line-height: 66px;
  }
  .headline-rule {
    position: absolute; left: 453px; top: 189px; width: 359px; height: 2px;
    background: #f1d9b8;
  }
  .tagline {
    position: absolute; right: 47px; top: 195px; width: 300px; text-align: right;
    color: var(--white); font-weight: 500; font-size: 19px; line-height: 23px;
  }

  .mission {
    position: absolute; left: 49px; top: 487px; width: 759px; height: 161px;
    background: var(--charcoal); color: var(--white); text-align: center;
    padding-top: 18px;
  }
  .mission h2 { font-weight: 500; font-size: 28px; line-height: 30px; }
  .mission p { font-weight: 500; font-size: 21px; line-height: 29px; margin-top: 3px; }

  .section-title {
    color: var(--red); font-weight: 600; font-size: 27px; line-height: 30px;
  }
  .coverages {
    position: absolute; right: 325px; top: 708px; text-align: right;
  }
  .carriers {
    position: absolute; left: 609px; top: 708px;
  }
  .item-list { list-style: none; margin-top: 12px; color: var(--ink); }
  .item-list li { font-weight: 500; font-size: 20px; line-height: 25px; }
  .item-list small { font-size: 13px; }
  .column-divider {
    position: absolute; left: 565px; top: 710px; width: 3px; height: 338px;
    background: var(--charcoal);
  }

  .brand {
    position: absolute; left: 45px; top: 962px;
    display: flex; align-items: center; gap: 16px;
  }
  .brand-mark { width: 58px; height: 58px; background: var(--red); }
  .brand-name {
    color: var(--white); font-weight: 600; font-size: 44px; line-height: 46px;
  }
  .website {
    position: absolute; left: 45px; top: 1112px;
    color: var(--white); font-weight: 600; font-size: 24px; letter-spacing: 2px;
  }

  .social { position: absolute; left: 660px; top: 1105px; display: flex; gap: 12px; }
  .social span {
    width: 42px; height: 42px; border-radius: 50%;
    border: 3px solid var(--red);
  }
</style>
</head>
<body>
<main class="flyer">
  <svg class="backdrop" width="859" height="1200" viewBox="0 0 859 1200">
    <defs>
      <linearGradient id="photoTone" x1="0" y1="0" x2="1" y2="1">
        <stop offset="0" stop-color="#4f5a52"/>
        <stop offset="0.5" stop-color="#3d4843"/>
        <stop offset="1" stop-color="#2e3438"/>
      </linearGradient>
    </defs>
    <rect class="hero-photo" x="0" y="0" width="859" height="520" fill="url(#photoTone)"
          role="img" aria-label="Photo of a smiling restaurant owner in an apron standing at his café entrance"/>
    <polygon class="hero-red-panel" points="195,0 859,0 859,490" fill="var(--red)" opacity="0.93"/>
    <polygon class="mission-underline" points="93,648 766,648 752,659 107,659" fill="var(--red)"/>
    <polygon class="footer-band" points="0,707 0,1200 663,1200" fill="var(--charcoal)"/>
  </svg>

  <h1 class="headline">Independent<br>Risk Advisors</h1>
  <div class="headline-rule"></div>
  <p class="tagline">Kovalen Brokerage believes in the ability of people to take control of their lives and of their future.</p>

  <section class="mission">
    <h2>OUR MISSION</h2>
    <p>Our mission is to provide insurance services and a risk<br>management plan at competitive prices while<br>offering superior personalized customer service.</p>
  </section>

  <section class="coverages">
    <h3 class="section-title">GENERAL LIABILITY</h3>
    <ul class="item-list">
      <li>FF&amp;E <small>(Furniture, Fixtures, and Equipment), Property</small></li>
      <li>Workers Compensation</li>
      <li>Umbrella</li>
      <li>Liquor Liability</li>
      <li>Auto</li>
      <li>Cyber</li>
      <li>Bonds</li>
      <li>EPLI</li>
    </ul>
  </section>

  <div class="column-divider"></div>

  <section class="carriers">
    <h3 class="section-title">CARRIER LIST:</h3>
    <ul class="item-list">
      <li>The Wexmoor</li>
      <li>Bastion</li>
      <li>Ferrow Common</li>
      <li>Wayfarers</li>
      <li>Plains Motor</li>
      <li>Quorra</li>
      <li>DELVA</li>
      <li>Holloway</li>
      <li>CountyFirst</li>
      <li>KTO</li>
      <li>Pelta</li>
      <li>and Many More</li>
    </ul>
  </section>

  <div class="brand">
    <span class="brand-mark"></span>
    <span class="brand-name">Kovalen<br>Brokerage</span>
  </div>
  <p class="website">www.kovalenbrokerage.example</p>

  <div class="social" aria-label="Social media links">
    <span></span><span></span><span></span>
  </div>
</main>
</body>
</html>
```